Nonprofit K-8 Korbane School. Elementary education ( please google Korbane Schools)

We are a nonprofit Korbane School in the U.S.
We need to advertise our school using yard signs. The information should be easy to see from a distance. Clear and concise, using large print without additional design outside of the logo itself. It should have our logo as the header, with the following text centered below the logo:
Open House!
Feb 10th, March 10th and April 21st.
Call 555 014-2967 for more information

Target Market(s)

Parents of children between ages of 5 yrs to 13yrs old

Industry/Entity Type

School

Other font styles liked:
• Formal436bt

Colors
ec1f27
ffffff

Requirements
Must have
• It must have our uploaded logo as the header, and the following information below using the font Formal436bt:
• Open House!
• Feb 10th, March 10th and April 21st.
• Call 555 014-2967 for more information
Should not have
• Any other color but the red and white indicated on our logo

```html
<!DOCTYPE html>
<html lang="en">
<head>
<meta charset="utf-8">
<title>Aldervale School – Open House Yard Sign</title>
<link rel="stylesheet" href="https://fonts.googleapis.com/css2?family=Cagliostro&family=Lato:wght@900&display=swap">
<style>
  :root {
    --sign-red: #ec1f27;
    --sign-red-deep: #b3192a;
    --sign-red-dark: #a01626;
    --sign-white: #ffffff;
    --backdrop: #d3d3d3;
  }
  * { box-sizing: border-box; margin: 0; padding: 0; }
  html, body {
    width: 1200px;
    height: 1200px;
    overflow: hidden;
    background: var(--backdrop);
  }
  .canvas {
    position: relative;
    width: 1200px;
    height: 1200px;
    display: flex;
    align-items: center;
    justify-content: center;
  }
  .yard-sign {
    width: 1140px;
    height: 714px;
    background:
      radial-gradient(ellipse 70% 60% at 50% 55%, var(--sign-red) 0%, rgba(236,31,39,0) 100%),
      linear-gradient(180deg, var(--sign-red-deep) 0%, var(--sign-red) 50%, var(--sign-red-dark) 100%);
    color: var(--sign-white);
    display: flex;
    flex-direction: column;
    align-items: center;
    font-family: "Cagliostro", sans-serif;
    text-align: center;
  }
  .school-name {
    margin-top: 104px;
    display: flex;
    align-items: center;
    gap: 18px;
    font-size: 44px;
    line-height: 1;
    letter-spacing: 0.5px;
    text-transform: uppercase;
  }
  .school-mark {
    width: 30px;
    height: 30px;
    background: var(--sign-white);
  }
  .headline {
    margin-top: 58px;
    font-size: 118px;
    line-height: 1;
    font-weight: 400;
  }
  .dates-band {
    margin-top: 44px;
    width: 1028px;
    height: 90px;
    background: var(--sign-white);
    color: var(--sign-red-dark);
    font-family: "Lato", sans-serif;
    font-weight: 900;
    font-size: 47px;
    display: flex;
    align-items: center;
    justify-content: center;
  }
  .info-label {
    margin-top: 40px;
    font-family: "Lato", sans-serif;
    font-weight: 900;
    font-size: 38px;
    line-height: 1;
  }
  .call-line {
    margin-top: 20px;
    font-size: 86px;
    line-height: 1;
    letter-spacing: 2px;
  }
</style>
</head>
<body>
  <main class="canvas">
    <section class="yard-sign">
      <header class="school-name">
        <span class="school-mark" aria-hidden="true"></span>
        <span>Aldervale School</span>
      </header>
      <h1 class="headline">OPEN House!</h1>
      <p class="dates-band">Feb 10th, March 10th and April 21st</p>
      <p class="info-label">FOR MORE INFORMATION</p>
      <p class="call-line">CALL 555 014-2967</p>
    </section>
  </main>
</body>
</html>
```